Recruitment of Brindle Staffing for the UK market

I want a website for the UK market to attract businesses and companies to come to us for Philipine labour. We want an information site that gives all information on what we do and how we can recruit Philippine labour.
This is a recruitment site for companies to contact us with their requirements for skilled workers coming from the Philipines over to the UK to work.

Target Market(s)

Uk Companies and businesses who want Philipine skilled workers

Industry/Entity Type

REcruitment

Coding

Coded - Design and coding required

Number of Pages Required

5+ page

Font styles to use
Sans Serif

Colors
0054AA
0677BA
7BADD7
CADEEF
E8F1F8
0094D4
00A9DD
6FCCEA
C7EBF8
E9F6FB
EE7325
F08F49
F5BC92
FAE3D3
FDF4ED
EB3D1F
EC4F4E
F09395
F8D3D4
FCEDEE

Requirements
Must have
• Look professional and corperate with drop down menus for Home ,about, services,articles. training , contact us
Nice to have
• Look at Tovel recruitment- https://tovelrecruitment.example.co.uk/. This is my current site - https://www.brindlestaffing.example.com/
Should not have
• Cartoons or silly pictures , needs to be corperate looking

```html
<!DOCTYPE html>
<html lang="en">
<head>
<meta charset="utf-8">
<title>Brindle Staffing — Skilled Philippine Workers for UK Companies</title>
<link href="https://fonts.googleapis.com/css2?family=Barlow:wght@400;500;600;700&display=swap" rel="stylesheet">
<style>
  :root{
    --red:#a51e12;
    --red-soft:#e7b9b4;
    --dark:#2b2b2b;
    --ink:#1e1e1e;
    --body:#444;
    --grey-bg:#f4f4f4;
    --line:#d9d9d9;
    --white:#fff;
  }
  *{box-sizing:border-box;margin:0;padding:0}
  html,body{width:1200px;height:4409px;overflow:hidden}
  body{font-family:"Barlow",Arial,sans-serif;color:var(--ink);background:var(--white);position:relative}
  .abs{position:absolute}
  .eyebrow{font-size:14px;letter-spacing:2px;color:var(--red);text-transform:uppercase;font-weight:500}
  .btn-outline{display:flex;align-items:center;justify-content:center;border:2px solid var(--red);color:var(--red);font-weight:600;letter-spacing:1px;text-transform:uppercase}

  /* header */
  .site-header{position:absolute;left:0;top:0;width:1200px;height:77px;background:var(--white);z-index:3}
  .brand{position:absolute;left:120px;top:20px;display:flex;align-items:center;gap:10px;font-size:26px;font-weight:700;color:var(--red)}
  .brand-mark{width:16px;height:16px;background:var(--red)}
  .main-nav{position:absolute;top:33px;left:425px;display:flex;font-size:13px;font-weight:500;color:#333;letter-spacing:.3px}
  .main-nav span{position:absolute;white-space:nowrap}
  .caret{display:inline-block;width:7px;height:7px;border-right:1.5px solid #555;border-bottom:1.5px solid #555;transform:rotate(45deg);margin-left:6px;position:relative;top:-3px}
  .header-contact{position:absolute;right:0;top:0;width:253px;height:77px;background:var(--red);clip-path:polygon(28px 0,100% 0,100% 100%,0 100%);color:var(--white)}
  .header-contact .label{position:absolute;left:80px;top:18px;font-size:12px;letter-spacing:.5px}
  .header-contact .phone{position:absolute;left:66px;top:32px;font-size:20px;font-weight:600;display:flex;align-items:center;gap:8px}
  .phone-dot{width:22px;height:22px;border-radius:50%;background:var(--white);display:flex;align-items:center;justify-content:center}

  /* hero */
  .hero{position:absolute;left:0;top:77px;width:1200px;height:642px;background:linear-gradient(90deg,#f2f2f2,#ececec)}
  .hero-photo{position:absolute;left:462px;top:0;width:738px;height:622px;background:linear-gradient(90deg,#ececec 0%,#d3dde6 30%,#8fb4da 60%,#5a8fc8 100%)}
  .scroll-cue{position:absolute;left:22px;top:310px;width:12px;height:170px}
  .scroll-cue span{position:absolute;left:0;top:0;transform:rotate(-90deg) translateX(-100%);transform-origin:0 0;font-size:10px;letter-spacing:3px;color:#444;white-space:nowrap}
  .scroll-cue i{position:absolute;left:6px;top:100px;width:1px;height:70px;background:var(--red)}
  .hero-frame{position:absolute;left:106px;top:158px;width:125px;height:279px;border:3px solid var(--red);border-right:none}
  .hero-frame::before,.hero-frame::after{content:"";position:absolute;right:-1px;width:0;height:28px;border-right:3px solid var(--red)}
  .hero-frame::before{top:-3px}.hero-frame::after{bottom:-3px}
  .hero-copy{position:absolute;left:142px;top:206px}
  .hero-copy .kicker{font-size:14px;letter-spacing:2px;color:#888}
  .hero-copy h1{margin-top:8px;font-size:36px;line-height:38.5px;font-weight:600;letter-spacing:1px;color:var(--ink)}
  .hero-copy h1 em{font-style:normal;color:var(--red)}

  /* service cards */
  .card{position:absolute;text-align:center;padding:0 20px}
  .card h3{font-size:20px;font-weight:500;letter-spacing:.6px;margin-top:12px}
  .card p{font-size:12px;line-height:20px;margin-top:10px}
  .card-help{left:132px;top:645px;width:306px;height:208px;background:var(--white);box-shadow:0 6px 24px rgba(0,0,0,.12);padding-top:28px;color:var(--ink)}
  .card-training{left:440px;top:621px;width:313px;height:232px;background:var(--red);color:var(--white);padding-top:30px}
  .card-contact{left:753px;top:645px;width:314px;height:208px;background:var(--dark);color:var(--white);padding-top:28px}
  .card-training .btn{display:inline-flex;margin-top:12px;width:120px;height:34px;align-items:center;justify-content:center;border:1.5px solid var(--white);font-size:11px;font-weight:600;letter-spacing:1px}

  /* about */
  .about-ring{position:absolute;left:103px;top:904px;width:514px;height:514px;border-radius:50%;border:1.5px solid var(--red-soft)}
  .about-photo{position:absolute;left:134px;top:935px;width:452px;height:452px;border-radius:50%;background:radial-gradient(circle at 50% 40%,#d8d4cc,#9ea6ac 70%,#6f7880)}
  .about-copy{position:absolute;left:659px;top:993px;width:460px}
  .eyebrow-line{display:flex;align-items:center;gap:12px}
  .eyebrow-line::after{content:"";width:70px;height:1.5px;background:var(--red);box-shadow:-6px 0 0 -0px transparent}
  .about-copy h2{font-size:30px;line-height:34px;font-weight:600;letter-spacing:1px;margin-top:10px}
  .about-copy p{font-size:16px;line-height:27px;color:var(--body);margin-top:16px;padding-left:4px}
  .about-copy .btn-outline{width:183px;height:55px;font-size:16px;margin-top:28px;margin-left:4px}

  /* working together */
  .divider-v{position:absolute;width:1.5px;background:var(--red)}
  .together{position:absolute;left:0;top:1494px;width:1200px;height:566px;background:var(--grey-bg);text-align:center}
  .together .eyebrow{position:absolute;left:0;right:0;top:60px}
  .together h2{position:absolute;left:0;right:0;top:94px;font-size:30px;font-weight:600;letter-spacing:1px;line-height:36px}
  .together h2 small{display:block;font-size:25px;font-weight:600;line-height:36px}
  .steps-line{position:absolute;left:253px;top:251px;width:687px;height:2px;background:#e2c8c5}
  .step{position:absolute;width:240px;text-align:center}
  .step .icon{width:86px;height:86px;border-radius:50%;margin:0 auto;display:flex;align-items:center;justify-content:center;position:relative}
  .step .icon::after{content:"";position:absolute;left:42px;top:86px;width:1.5px;height:24px;background:var(--red)}
  .step h3{font-size:19px;font-weight:500;letter-spacing:.5px;margin-top:32px}
  .step p{font-size:12px;line-height:20.5px;color:var(--body);margin-top:8px}
  .step a{display:inline-block;margin-top:12px;font-size:11px;font-weight:600;color:#333;text-decoration:underline;letter-spacing:.5px}

  /* skilled workers */
  .workers{position:absolute;left:0;top:2060px;width:1200px;height:582px;background:var(--red);color:var(--white)}
  .workers .eyebrow{color:var(--white)}
  .workers .eyebrow-line::after{background:var(--white)}
  .workers-copy{position:absolute;left:142px;top:140px;width:420px}
  .workers-copy h2{font-size:29px;font-weight:600;letter-spacing:1px;margin-top:8px}
  .workers-copy p{font-size:16.5px;line-height:27px;margin-top:14px}
  .workers-copy .btn{display:flex;align-items:center;justify-content:center;width:150px;height:44px;border:2px solid var(--white);font-size:13px;font-weight:600;letter-spacing:1px;margin-top:30px}
  .workers-frame{position:absolute;left:599px;top:2166px;width:545px;height:556px;border:1.5px solid var(--red-soft)}
  .workers-photo{position:absolute;left:618px;top:2179px;width:514px;height:533px;background:linear-gradient(160deg,#55595c 0%,#3b3f43 45%,#8b8f92 100%)}

  /* training */
  .training{position:absolute;left:0;top:2642px;width:1200px;height:739px;background:var(--grey-bg);text-align:center}
  .training .eyebrow{position:absolute;left:0;right:0;top:132px}
  .training h2{position:absolute;left:0;right:0;top:158px;font-size:38px;font-weight:600;letter-spacing:1.5px}
  .training p{position:absolute;left:210px;width:780px;top:222px;font-size:16.5px;line-height:29px;color:var(--body)}
  .training-photo{position:absolute;left:0;top:378px;width:1200px;height:361px;background:linear-gradient(90deg,#c9bfb5 0%,#e9e6e2 35%,#d9d4cf 60%,#b69a86 100%)}
  .training .btn-outline{position:absolute;left:519px;top:325px;width:159px;height:41px;font-size:12px;background:var(--grey-bg);z-index:1}

  /* contact */
  .contact-copy{position:absolute;left:152px;top:3480px}
  .contact-copy h2{font-size:31px;font-weight:600;letter-spacing:1px;margin-top:6px}
  .field{position:absolute;left:147px;width:483px;height:55px;border:1.5px solid #aab3bd;font-size:15px;color:#555;padding:16px 0 0 22px}
  .field.message{height:98px}
  .send-btn{position:absolute;left:149px;top:3883px;width:195px;height:46px;background:var(--red);color:var(--white);font-size:14px;font-weight:600;letter-spacing:1px;display:flex;align-items:center;justify-content:center}
  .map{position:absolute;left:690px;top:3398px;width:354px;height:582px;border-radius:40% 30% 45% 35%;background:radial-gradient(ellipse at 50% 50%,#ddb7b5,#ecd3d1 70%,#fff 100%)}

  /* footer */
  .site-footer{position:absolute;left:0;top:4032px;width:1200px;height:377px;background:var(--grey-bg)}
  .footer-brand{position:absolute;left:142px;top:72px;display:flex;align-items:center;gap:10px;font-size:26px;font-weight:700;color:var(--red)}
  .socials{position:absolute;left:146px;top:146px;display:flex;gap:6px}
  .socials span{width:31px;height:31px;border-radius:50%;background:var(--dark)}
  .footer-col{position:absolute;top:11px;height:203px;border-left:1.5px solid var(--red-soft);padding:60px 0 0 14px}
  .footer-col h4{font-size:14px;font-weight:600;letter-spacing:.5px;position:relative}
  .footer-col h4::before{content:"";position:absolute;left:-14px;top:-2px;width:3px;height:20px;background:var(--red)}
  .footer-col ul{list-style:none;margin-top:10px;margin-left:6px}
  .footer-col li{font-size:13px;line-height:26px;color:#333}
  .contact-line{position:absolute;display:flex;align-items:flex-start;gap:14px;font-size:13px;font-weight:500;color:#222;line-height:20px}
  .contact-line .dot{flex:none;width:30px;height:30px;border-radius:50%;background:var(--red);display:flex;align-items:center;justify-content:center}
  .footer-rule{position:absolute;left:0;top:299px;width:1200px;height:1px;background:var(--line)}
  .copyright{position:absolute;left:0;right:0;top:322px;text-align:center;font-size:12px;color:#444}
</style>
</head>
<body>

<header class="site-header">
  <div class="brand"><span class="brand-mark"></span>Brindle Staffing</div>
  <nav class="main-nav">
    <span style="left:0">ABOUT</span>
    <span style="left:88px">SERVICES<i class="caret"></i></span>
    <span style="left:193px">ARTICLES</span>
    <span style="left:297px">TRAINING<i class="caret"></i></span>
    <span style="left:396px">CONTACT US</span>
  </nav>
  <div class="header-contact">
    <div class="label">CONTACT TODAY</div>
    <div class="phone"><span class="phone-dot"><svg width="12" height="12" viewBox="0 0 24 24"><path fill="#a51e12" d="M6.6 10.8a15 15 0 0 0 6.6 6.6l2.2-2.2c.3-.3.7-.4 1-.2 1.1.4 2.3.6 3.6.6.6 0 1 .4 1 1V20c0 .6-.4 1-1 1A17 17 0 0 1 3 4c0-.6.4-1 1-1h3.5c.6 0 1 .4 1 1 0 1.3.2 2.5.6 3.6.1.3 0 .7-.2 1z"/></svg></span>07700 900418</div>
  </div>
</header>

<section class="hero">
  <div class="hero-photo" role="img" aria-label="Team of smiling healthcare workers in blue scrubs"></div>
  <div class="scroll-cue"><span>SCROLL DOWN</span><i></i></div>
  <div class="hero-frame"></div>
  <div class="hero-copy">
    <div class="kicker">BRINDLE STAFFING</div>
    <h1>RECRUITING AND PLACING<br>SKILLED PHILIPPINE<br><em>WORKERS INTO<br>UK COMPANIES</em></h1>
  </div>
</section>

<div class="card card-help">
  <svg width="40" height="40" viewBox="0 0 40 40" fill="none" stroke="#a51e12" stroke-width="1.8"><circle cx="20" cy="12" r="6"/><path d="M11 24c2-4 5-5 9-5s7 1 9 5"/><path d="M6 30l8-3 8 2h6l6-4"/><path d="M6 34h28"/></svg>
  <h3>HOW WE HELP</h3>
  <p>We work with companies to find skilled workers that meet the UK requirements</p>
</div>
<div class="card card-training">
  <svg width="40" height="40" viewBox="0 0 40 40" fill="none" stroke="#fff" stroke-width="1.8"><rect x="8" y="6" width="22" height="28" rx="2"/><path d="M13 13h12M13 19h12M13 25h8"/><path d="M28 26l6 6"/></svg>
  <h3>OUR TRAINING</h3>
  <p>We need to know what your issues are and how we can understand the personnal you require</p>
  <span class="btn">LEARN MORE</span>
</div>
<div class="card card-contact">
  <svg width="40" height="40" viewBox="0 0 40 40" fill="none" stroke="#fff" stroke-width="1.8"><rect x="6" y="10" width="24" height="24" rx="2"/><path d="M11 18h10M11 24h8"/><path d="M22 26l12-18 3 2-12 18-4 1z"/></svg>
  <h3>CONTACT US TODAY</h3>
  <p>Please contact us today with your requirements , this can be care workers</p>
</div>

<div class="about-ring"></div>
<div class="about-photo" role="img" aria-label="Group of workers from different trades and professions standing together"></div>
<div class="about-copy">
  <div class="eyebrow eyebrow-line">WHO WE ARE</div>
  <h2>WHAT THE<br>BUSINESS IS ABOUT</h2>
  <p>We source skilled workers directly from the Philippines to work in the UK. With offices , training locations and specialist recruiters we can find the highest quality individuals to add value and resources to any UK buisness. We delivery quality based on vast experience over a number of years.</p>
  <div class="btn-outline">LEARN MORE</div>
</div>

<div class="divider-v" style="left:596px;top:1464px;height:56px;z-index:2"></div>

<section class="together">
  <div class="eyebrow">WORKING TOGETHER</div>
  <h2>WE RECRUIT THE FINEST TALENT AVAILABLE<small>WITH OUR DEDICATED 200 STRONG TEAM</small></h2>
  <div class="steps-line"></div>
  <div class="step" style="left:133px;top:209px">
    <div class="icon" style="background:#fff">
      <svg width="44" height="44" viewBox="0 0 44 44" fill="none" stroke="#a51e12" stroke-width="1.8"><circle cx="14" cy="14" r="8"/><circle cx="30" cy="14" r="8"/><circle cx="14" cy="30" r="8"/><circle cx="30" cy="30" r="8"/></svg>
    </div>
    <h3>WHAT WE DO</h3>
    <p>Our company has been estabilished in the Philippines for over 20 years. We have mainly been recruiting philippine workers for the off shore industry</p>
    <a>LEARN MORE</a>
  </div>
  <div class="step" style="left:477px;top:209px">
    <div class="icon" style="background:var(--red)">
      <svg width="44" height="44" viewBox="0 0 44 44" fill="none" stroke="#fff" stroke-width="1.8"><circle cx="22" cy="14" r="6"/><circle cx="11" cy="18" r="4"/><circle cx="33" cy="18" r="4"/><path d="M12 32c1-6 5-9 10-9s9 3 10 9"/></svg>
    </div>
    <h3 style="margin-top:38px">HOW WE HELP</h3>
    <p>We work with companies to find skilled workers that meet the UK requirements for Visas and work permits. We guide you through the whole process</p>
    <a>LEARN MORE</a>
  </div>
  <div class="step" style="left:820px;top:209px">
    <div class="icon" style="background:var(--dark)">
      <svg width="44" height="44" viewBox="0 0 44 44" fill="none" stroke="#fff" stroke-width="1.8"><circle cx="17" cy="25" r="8"/><circle cx="17" cy="25" r="3"/><circle cx="30" cy="14" r="6"/><circle cx="30" cy="14" r="2"/><path d="M17 14v3M17 33v3M6 25h3M25 25h3M30 5v3M30 20v3M21 14h3M36 14h3"/></svg>
    </div>
    <h3 style="margin-top:38px">WHERE TO START</h3>
    <p>We need to know what your issues are and how we can understand the person-nal you require , over what time frame and the number of employees you need.</p>
    <a>LEARN MORE</a>
  </div>
</section>

<section class="workers">
  <div class="workers-copy">
    <div class="eyebrow eyebrow-line">ABOUT WORKERS</div>
    <h2>UK SKILLED WORKERS LIST</h2>
    <p>The UK government since brexit have developed a new system based on points (similar to Australia) when re-cruiting from outside of the UK. Previously EU citizens could work in the UK without any extensive documen-tation or clarification of skills. This has all changed. Overseas recruitment must now focus on skills that are currently short in the UK.</p>
    <div class="btn">LEARN MORE</div>
  </div>
</section>
<div class="workers-frame"></div>
<div class="workers-photo" role="img" aria-label="Industrial workers in hard hats standing with arms crossed in a factory"></div>

<section class="training">
  <div class="eyebrow">WHO WE ARE</div>
  <h2>OUR TRAINING</h2>
  <p>We source skilled workers directly from the Philippines to work in the UK. With offices , training loca-tions and specialist recruiters we can find the highest quality individuals to add value and resources to any UK buisness. We delivery quality based on vast experience over a number of years.</p>
  <div class="btn-outline">LEARN MORE</div>
  <div class="training-photo" role="img" aria-label="Two professionals talking in a bright office lounge with a laptop"></div>
</section>

<div class="divider-v" style="left:596px;top:3381px;height:31px"></div>

<section class="contact" aria-label="Contact">
  <div class="contact-copy">
    <div class="eyebrow">OUR LOCATION</div>
    <h2>CONTACT US TODAY</h2>
  </div>
  <div class="field" style="top:3564px">Name*</div>
  <div class="field" style="top:3633px">Email address*</div>
  <div class="field" style="top:3701px">Phone*</div>
  <div class="field message" style="top:3766px">Message</div>
  <div class="send-btn">SEND MESSAGE</div>
  <div class="map" role="img" aria-label="Map of the Philippines with regional boundaries"></div>
</section>

<footer class="site-footer">
  <div class="footer-brand"><span class="brand-mark"></span>Brindle Staffing</div>
  <div class="socials">
    <span role="img" aria-label="Social link"></span>
    <span role="img" aria-label="Social link"></span>
    <span role="img" aria-label="Social link"></span>
    <span role="img" aria-label="Social link"></span>
  </div>
  <div class="footer-col" style="left:437px">
    <h4>QUICK LINKS</h4>
    <ul><li>Home</li><li>About Us</li><li>Services</li><li>Training</li></ul>
  </div>
  <div class="footer-col" style="left:618px">
    <h4>RESOURCES</h4>
    <ul><li>Why Us?</li><li>Faq</li><li>Blogs</li><li>Privacy Policy</li></ul>
  </div>
  <div class="footer-col" style="left:842px">
    <h4>CONTACT US</h4>
  </div>
  <div class="contact-line" style="left:857px;top:110px">
    <span class="dot"><svg width="14" height="14" viewBox="0 0 24 24"><path fill="#fff" d="M12 2a7 7 0 0 0-7 7c0 5 7 13 7 13s7-8 7-13a7 7 0 0 0-7-7zm0 9.5A2.5 2.5 0 1 1 12 6.5a2.5 2.5 0 0 1 0 5z"/></svg></span>
    <span style="font-weight:400">123 Lorem Ipsum Address line<br>tempor incididunt ut la</span>
  </div>
  <div class="contact-line" style="left:857px;top:158px;align-items:center">
    <span class="dot"><svg width="13" height="13" viewBox="0 0 24 24"><path fill="#fff" d="M6.6 10.8a15 15 0 0 0 6.6 6.6l2.2-2.2c.3-.3.7-.4 1-.2 1.1.4 2.3.6 3.6.6.6 0 1 .4 1 1V20c0 .6-.4 1-1 1A17 17 0 0 1 3 4c0-.6.4-1 1-1h3.5c.6 0 1 .4 1 1 0 1.3.2 2.5.6 3.6.1.3 0 .7-.2 1z"/></svg></span>
    <span>(555) 308-5202</span>
  </div>
  <div class="contact-line" style="left:857px;top:212px;align-items:center">
    <span class="dot"><svg width="14" height="14" viewBox="0 0 24 24" fill="none" stroke="#fff" stroke-width="2"><rect x="3" y="6" width="18" height="12" rx="1"/><path d="M3 7l9 6 9-6"/></svg></span>
    <span>hello@brindlestaffing.example.com</span>
  </div>
  <div class="footer-rule"></div>
  <div class="copyright">© 2023 All Rights Reserved | Brindle Staffing Ltd</div>
</footer>

</body>
</html>
```